WebDesign | Financial Services Firm - Risk Mitigation

We are a professional services consulting firm that specializes in high net worth individuals over $25,000,000, executives C-suite and above, closely held businesses owners, family offices and highly compensated employees.

Our focus is on risk mitigation and tax efficient strategies. Our clients take their risk on themselves and have a proven track record generating wealth. Our directive is to preserve and protect the wealth they’ve already created.

Our company Harbinger Collective is geared around five directives of asset protection:
1) Legal Structuring
2) Leverage & Financing
3) Risk Management - Asset Protection & Insurance, Trustee Work
4) Asset Management & Investing - Under www.dvkfarcoast.com
5) Tax Efficient Strategies

Our Company Mark is a Pentagon with a key in the middle. A pentagon is the most efficient defensive structure. Each point of a pentagon is equal distance front every point . Each side provides support to another and works together, which is the key to our clients success.

Our key colors are blue, black and silver.

We ‘re located in the Pacific Northwest with bi coastal and international clients. We have fewer, higher net worth clients and provide exceptional customer service. We do not do social media.

We'll need the following pages:
-Front Landing Page.
Front page has to have link to hcportal.filevaultly.net for logging into secure site.
- Contact & About Us Page
- Our Team Page
- Five Sides of Wealth Management
> Legal & Business Structuring
> Leverage & Financing
> Risk Management & Asset Protection.
> Asset Management and Investing - Will link to DVK (won't be turned on for a few months)
> Tax Efficient Strategies.

Industry/Entity Type

Financial Service

Coding

Coded - Design and coding required

Number of Pages Required

5+ page

Font styles to use
Sans Serif

Colors
0555a3

Requirements
Must have
• Our key colors are blue, black and silver.

-Front Landing Page.
- Contact & About Us Page
- Our Team Page
> Leverage & Financing
Nice to have
• I have attached images that have been purchased for use on the webpage. Us or not.

location page: 872 W Birchwood Ave, Suite 114, Lake Oswego, OR 97035
Should not have
• lots of color.

```html
<!DOCTYPE html>
<html lang="en">
<head>
<meta charset="utf-8">
<title>Harbinger Collective — Risk Mitigation &amp; Tax Efficient Strategies</title>
<link href="https://fonts.googleapis.com/css2?family=Cinzel:wght@400;600;700&family=Poppins:wght@400;500;600&display=swap" rel="stylesheet">
<style>
:root{
  --blue:#0555a3;
  --ink:#111;
  --text:#444;
  --pale:#eef5fc;
  --white:#fff;
}
*{box-sizing:border-box;margin:0;padding:0}
html,body{width:1200px;height:3168px;overflow:hidden}
body{position:relative;background:var(--white);font-family:'Poppins',sans-serif;color:var(--text)}
.abs{position:absolute}
.serif{font-family:'Cinzel',serif}

.topbar{left:0;top:0;width:1200px;height:37px;background:var(--blue);color:var(--white);font-size:14px;font-weight:500}
.topbar .item{top:9px;display:flex;align-items:center;gap:8px}
.nav{left:0;top:37px;width:1200px;height:76px;background:var(--white)}
.nav a{position:absolute;top:30px;font-family:'Cinzel',serif;font-size:14px;color:#222;text-decoration:none;letter-spacing:.5px}
.nav a.active{color:var(--blue);font-weight:600}
.nav .login{top:20px;left:948px;width:90px;height:36px;border:1.5px solid var(--blue);color:var(--blue);font-weight:600;display:flex;align-items:center;justify-content:center;border-radius:2px}
.brand-tab{left:502px;top:0;width:196px;height:133px;background:var(--white);clip-path:polygon(0 0,100% 0,96% 100%,4% 100%);z-index:3;display:flex;flex-direction:column;align-items:center;justify-content:flex-end;padding-bottom:16px}
.brand-tab .mark{width:34px;height:34px;background:var(--blue);margin-bottom:14px}
.brand-tab .name{font-family:'Cinzel',serif;font-weight:700;color:var(--blue);font-size:18px;line-height:1.1;text-align:center}

.hero{left:0;top:113px;width:1200px;height:526px;background:linear-gradient(180deg,#3a3f86 0%,#6a5c9a 30%,#b9847f 50%,#3a3b45 72%,#1d2024 100%)}
.hero-title{left:0;top:497px;width:1200px;text-align:center;color:var(--white);font-family:'Cinzel',serif;font-weight:400;font-size:44px;line-height:50px;letter-spacing:1px}

.about-accent-light{left:440px;top:744px;width:170px;height:170px;border-radius:50%;background:#c5dcf7}
.about-accent-blue{left:150px;top:998px;width:172px;height:172px;border-radius:50%;background:var(--blue)}
.about-photo{left:160px;top:730px;width:448px;height:448px;border-radius:50%;background:radial-gradient(circle at 60% 55%,#c9a36a 0%,#8f7c86 35%,#a98cc0 60%,#6f8a6f 85%,#c48a8e 100%)}
.about-title{left:653px;top:796px;color:var(--blue);font-family:'Cinzel',serif;font-weight:400;font-size:34px;line-height:40px}
.about-title b{font-weight:700}
.about-lead{left:653px;top:888px;width:400px;color:var(--ink);font-size:17px;font-weight:500;line-height:26px}
.about-body{left:653px;top:949px;width:395px;font-size:14px;line-height:24.5px}
.btn-outline{border:1.5px solid var(--blue);color:var(--blue);font-family:'Cinzel',serif;font-weight:600;font-size:14px;display:flex;align-items:center;justify-content:center;border-radius:3px;background:var(--white)}
.about-btn{left:653px;top:1066px;width:120px;height:37px}

.services{left:0;top:1275px;width:1200px;height:1033px;background:var(--pale)}
.services-title{left:0;top:1366px;width:1200px;text-align:center;font-family:'Cinzel',serif;font-weight:400;font-size:38px;color:var(--blue)}
.services-title b{font-weight:700}
.card{width:268px;height:334px;background:var(--white);border-radius:0 0 26px 26px;overflow:hidden;box-shadow:0 4px 18px rgba(5,85,163,.06)}
.card::before{content:"";position:absolute;left:0;top:0;width:54px;height:54px;background:var(--blue);clip-path:polygon(0 0,100% 0,0 100%)}
.card svg{position:absolute;left:34px;top:48px;width:62px;height:62px}
.card h3{position:absolute;left:35px;top:130px;width:220px;font-family:'Cinzel',serif;font-weight:400;font-size:19px;line-height:23px;color:var(--ink);letter-spacing:.5px}
.card p{position:absolute;left:35px;top:184px;width:210px;font-size:13px;line-height:20px;color:#444}
.card .more{position:absolute;left:35px;top:288px;font-size:13px;font-weight:600;color:var(--blue)}
.ghost-name{left:466px;top:1930px;width:268px;text-align:center;font-family:'Cinzel',serif;font-weight:700;font-size:28px;line-height:34px;color:#d9dee5}
.services-btn{left:510px;top:2182px;width:180px;height:37px}

.cta{left:0;top:2308px;width:1200px;height:436px;background:linear-gradient(180deg,#ffffff 0%,#f1f4f7 40%,#dfe4ea 62%,#8c949d 82%,#5d646c 100%)}
.cta-title{left:0;top:2402px;width:1200px;text-align:center;font-family:'Cinzel',serif;font-weight:600;font-size:29px;line-height:36px;color:var(--blue);letter-spacing:.5px}
.cta-text{left:200px;top:2446px;width:800px;text-align:center;font-size:17px;line-height:25px;color:#333}
.btn-solid{left:510px;top:2514px;width:180px;height:36px;background:var(--blue);color:var(--white);font-family:'Cinzel',serif;font-weight:600;font-size:14px;display:flex;align-items:center;justify-content:center;border-radius:2px}

.footer{left:0;top:2744px;width:1200px;height:385px;background:var(--blue)}
.foot-head{color:var(--white);font-family:'Cinzel',serif;font-weight:400;font-size:17px;letter-spacing:.5px}
.rule{width:30px;height:2px;background:var(--white)}
.links{list-style:none;font-size:14px;color:var(--white)}
.links li{height:32.5px}
.links li::before{content:"›";margin-right:8px}
.footer-mark{left:582px;top:2878px;width:36px;height:36px;border:3px solid var(--white)}
.footer-brand{left:420px;top:2960px;width:360px;text-align:center;font-family:'Cinzel',serif;font-weight:700;font-size:38px;line-height:44px;color:var(--white)}
.contact-row{display:flex;gap:10px;width:200px;color:var(--white)}
.contact-row .ic{flex:0 0 24px;height:24px;border-radius:50%;background:var(--white);display:flex;align-items:center;justify-content:center}
.contact-row .t{font-size:12.5px;line-height:17px}
.contact-row .t strong{display:block;font-size:13.5px;font-weight:500}
.contact-row .t strong.serif{font-family:'Cinzel',serif;font-weight:400}
.copyright{left:0;top:3129px;width:1200px;height:39px;background:#111;color:#ddd;font-size:14px;display:flex;align-items:center;justify-content:center}
</style>
</head>
<body>

<header>
  <div class="abs topbar">
    <div class="abs item" style="left:163px">
      <svg width="14" height="14" viewBox="0 0 24 24" fill="#fff"><path d="M6.6 10.8a15.1 15.1 0 006.6 6.6l2.2-2.2a1 1 0 011-.25 11.4 11.4 0 003.6.57 1 1 0 011 1V20a1 1 0 01-1 1A17 17 0 013 4a1 1 0 011-1h3.5a1 1 0 011 1c0 1.25.2 2.45.57 3.6a1 1 0 01-.25 1z"/></svg>
      555 014 2290
    </div>
    <div class="abs item" style="left:878px">
      <svg width="14" height="14" viewBox="0 0 24 24" fill="#fff"><path d="M22 2L2 11l7 3 3 7z"/></svg>
      hello@harbingerco.net
    </div>
  </div>

  <nav class="abs nav">
    <a class="active" style="left:164px">HOME</a>
    <a style="left:268px">ABOUT US</a>
    <a style="left:399px">SERVICES</a>
    <a style="left:716px">OUR TEAM</a>
    <a style="left:823px">CONTACT US</a>
    <a class="login" href="https://hcportal.filevaultly.net">LOGIN</a>
  </nav>
  <div class="abs brand-tab">
    <span class="mark"></span>
    <span class="name">HARBINGER<br>COLLECTIVE</span>
  </div>
</header>

<section>
  <div class="abs hero" role="img" aria-label="Evening street with a brick corner building under a purple and orange dusk sky"></div>
  <h1 class="abs hero-title">We focus on risk mitigation and<br>tax efficient strategies.</h1>
</section>

<section>
  <div class="abs about-accent-light"></div>
  <div class="abs about-accent-blue"></div>
  <div class="abs about-photo" role="img" aria-label="Stacks of coins resting on euro banknotes"></div>
  <h2 class="abs about-title">ABOUT<br><b>HARBINGER COLLECTIVE</b></h2>
  <p class="abs about-lead">Lorem Ipsum dolor sit amet consectetuer adipiscing elit sed diam nonummy.</p>
  <p class="abs about-body">Ut wisi enim ad minim veniam, quis nostrud exerci tation ullam corper suscipit lobortis nisl ut aliquip ex ea mmodo consequat. Duis autem vel eum iriure dolor in hendrerit in utatel velit esse molestie.</p>
  <a class="abs btn-outline about-btn">READ MORE</a>
</section>

<section>
  <div class="abs services"></div>
  <h2 class="abs services-title">OUR <b>SERVICES</b></h2>

  <article class="abs card" style="left:172px;top:1447px">
    <svg viewBox="0 0 64 64" fill="none" stroke="#0555a3" stroke-width="2.4"><rect x="4" y="4" width="40" height="52" rx="3"/><path d="M12 30V20M20 30V14M28 30V22M10 42h14M10 48h10"/><circle cx="46" cy="44" r="10"/><path d="M53 51l7 7M42 48l8-8"/></svg>
    <h3>Tax Efficient Strategies</h3>
    <p>Lorem ipsum dolor sit amet, consectetuer adipiscing elit, sed diam nonummy nibh euismod tincidunt ut laoreet</p>
    <span class="more">Know More</span>
  </article>

  <article class="abs card" style="left:466px;top:1447px">
    <svg viewBox="0 0 64 64" fill="none" stroke="#0555a3" stroke-width="2.4"><rect x="6" y="4" width="38" height="52" rx="3"/><path d="M14 14h22M14 22h22M14 30h14"/><circle cx="18" cy="44" r="6"/><path d="M15 44l2 2 4-4"/><circle cx="48" cy="40" r="7"/><path d="M40 60v-6a8 8 0 0116 0v6z"/></svg>
    <h3>Legal &amp; Business Structuring</h3>
    <p>Lorem ipsum dolor sit amet, consectetuer adipiscing elit, sed diam nonummy nibh euismod tincidunt ut laoreet</p>
    <span class="more">Know More</span>
  </article>

  <article class="abs card" style="left:759px;top:1447px">
    <svg viewBox="0 0 64 64" fill="none" stroke="#0555a3" stroke-width="2.4"><path d="M8 4v16l-4-4M8 20l4-4M20 4v16"/><circle cx="46" cy="14" r="10"/><path d="M46 8v12"/><rect x="6" y="30" width="20" height="6"/><rect x="6" y="38" width="20" height="6"/><rect x="6" y="46" width="20" height="6"/><rect x="36" y="34" width="20" height="6"/><rect x="36" y="42" width="20" height="6"/><rect x="36" y="50" width="20" height="6"/></svg>
    <h3>Leverage &amp; Financing</h3>
    <p>Lorem ipsum dolor sit amet, consectetuer adipiscing elit, sed diam nonummy nibh euismod tincidunt ut laoreet</p>
    <span class="more">Know More</span>
  </article>

  <article class="abs card" style="left:172px;top:1807px">
    <svg viewBox="0 0 64 64" fill="none" stroke="#0555a3" stroke-width="2.4"><rect x="4" y="16" width="44" height="32" rx="2"/><path d="M20 48v8M32 48v8M14 56h24M18 38l8-14 8 14z M26 30v4"/><circle cx="50" cy="14" r="8"/><circle cx="50" cy="14" r="3"/></svg>
    <h3>Risk Management &amp; Asset Protection</h3>
    <p>Lorem ipsum dolor sit amet, consectetuer adipiscing elit, sed diam nonummy nibh euismod tincidunt ut laoreet</p>
    <span class="more">Know More</span>
  </article>

  <div class="abs ghost-name">HARBINGER<br>COLLECTIVE</div>

  <article class="abs card" style="left:759px;top:1807px">
    <svg viewBox="0 0 64 64" fill="none" stroke="#0555a3" stroke-width="2.4"><path d="M4 44h10l10 4h14a4 4 0 010 8H24M4 60h30l24-12a4 4 0 00-4-6L40 48"/><rect x="14" y="8" width="14" height="22" rx="4"/><rect x="32" y="4" width="10" height="26"/><rect x="42" y="12" width="12" height="18"/></svg>
    <h3>Asset Management and Investing</h3>
    <p>Lorem ipsum dolor sit amet, consectetuer adipiscing elit, sed diam nonummy nibh euismod tincidunt ut laoreet</p>
    <span class="more">Know More</span>
  </article>

  <a class="abs btn-outline services-btn">CONTACT US TODAY</a>
</section>

<section>
  <div class="abs cta" role="img" aria-label="City skyline along a waterfront under a pale cloudy sky"></div>
  <h2 class="abs cta-title">We are a professional services consulting firm</h2>
  <p class="abs cta-text">specializes in high net worth individuals over $25,000,000, executives C-suite and above, closely held businesses owners, family offices and highly compensated employees.</p>
  <a class="abs btn-solid">CONTACT US TODAY</a>
</section>

<footer>
  <div class="abs footer"></div>
  <h4 class="abs foot-head" style="left:162px;top:2838px">QUICK LINKS</h4>
  <div class="abs rule" style="left:162px;top:2870px"></div>
  <ul class="abs links" style="left:162px;top:2893px">
    <li>Home</li><li>About Us</li><li>Services</li><li>Our Team</li><li>Contact Us</li>
  </ul>

  <div class="abs footer-mark"></div>
  <div class="abs footer-brand">HARBINGER<br>COLLECTIVE</div>

  <h4 class="abs foot-head" style="left:847px;top:2838px">Contact Details</h4>
  <div class="abs rule" style="left:847px;top:2870px"></div>
  <div class="abs contact-row" style="left:847px;top:2887px">
    <span class="ic"><svg width="12" height="12" viewBox="0 0 24 24" fill="#0555a3"><path d="M12 2a7 7 0 00-7 7c0 5 7 13 7 13s7-8 7-13a7 7 0 00-7-7zm0 9.5A2.5 2.5 0 1112 6.5a2.5 2.5 0 010 5z"/></svg></span>
    <span class="t"><strong class="serif">Harbinger Collective</strong>872 W Birchwood Ave, Suite 114, Lake Oswego, OR 97035</span>
  </div>
  <div class="abs contact-row" style="left:847px;top:2960px">
    <span class="ic"><svg width="12" height="12" viewBox="0 0 24 24" fill="#0555a3"><path d="M6.6 10.8a15.1 15.1 0 006.6 6.6l2.2-2.2a1 1 0 011-.25 11.4 11.4 0 003.6.57 1 1 0 011 1V20a1 1 0 01-1 1A17 17 0 013 4a1 1 0 011-1h3.5a1 1 0 011 1c0 1.25.2 2.45.57 3.6a1 1 0 01-.25 1z"/></svg></span>
    <span class="t"><strong>Call Us</strong>555 014 2290</span>
  </div>
  <div class="abs contact-row" style="left:847px;top:3012px">
    <span class="ic"><svg width="12" height="12" viewBox="0 0 24 24" fill="#0555a3"><path d="M22 2L2 11l7 3 3 7z"/></svg></span>
    <span class="t"><strong>Mail Us</strong>hello@harbingerco.net</span>
  </div>

  <div class="abs copyright">Copyright © 2021 Harbinger Collective. All Rights Reserved.</div>
</footer>

</body>
</html>
```